Upscale, Elegant Healthy Turmeric Honey Packaging Project for a Startup

We are a startup company based in North Carolina, US. We focus on benefits of Turmeric. We are looking for a packaging design that is elegant, clean looking mostly on white background which would standout on shelf as well as speak to quality of the ingredients and product.Few important points about our product1) All our ingredients are 100% USDA Organic2) Two Types of Honey - 100% Raw Unfiltered Wildflower Honey (Local). It needs to say Made by North Carolina Bees" to stand out as local honey - 100% Organic Raw Honey (non-localized)3) Our honey includes actual raw turmeric roots so this is important to communicate which is the key factor of our product4) We use Hex bottle of 12 Oz and 16 oz classic jar bottleFinal design should be clean, healthy and upscale - should be flexible to accommodate types of honey. 5 ) Back label image is attached. Our organic honey is from Brazil so Product of Brazil or Product of the USA is added to each of the back label.6) Website name needs to be in front of the label and our new website soon to be launch will be www.GoldenSpoonHive.com 7) We have tag line "Saffrola! Bring it to your day!" which is our registered trademark needs to be included in back or front label (help us choose)We have attached some of the current simple example of our labels that we use. Provide design how it would look in the two types of bottles.

Please try to show on a bottle image of bottle (illustration) we use
https://www.jarvillestore.com/glass-containers/kq4d-classic-glass-jar-1lb.asp for 8 oz and 16 oz
and we use
https://www.jarvillestore.com/glass-containers/pm7r-12oz-hex-jars-w-63mm-cap.asp for 12 oz

Target Market(s)

upscale retailers, consumers, health & wealth

Colors
fcf9ce
fffbf1
fbca95
ffffff
fefdec

Requirements
Must have
• Clean, elegant look, We prefer white or off white background, Must have way to show that our honey includes raw turmeric or somehow to communicate it is turmeric honey.
Should not have
• Absolutely no similar concept of our current labels should be used in new design. Whole idea is that we are open to adopt creative ways to communicate to our customer about our product so take this as challenge.

```html
<!DOCTYPE html>
<html lang="en">
<head>
<meta charset="utf-8">
<title>Honey Label Range</title>
<link href="https://fonts.googleapis.com/css2?family=Marcellus+SC&family=Montserrat:wght@600;700&display=swap" rel="stylesheet">
<style>
  :root {
    --backdrop: #e4e4e4;
    --label-white: #ffffff;
    --ink-dark: #1c1c1c;
    --brand-green: #6aa535;
    --sage-band: #c4dccb;
    --sage-soft: #eef4ef;
    --blush-band: #ecc5b6;
    --blush-soft: #fbeeea;
    --cinnamon: #7a1212;
    --peach-band: #f9cc96;
    --peach-soft: #fdf1e3;
    --turmeric: #ef7a1d;
  }
  * { box-sizing: border-box; margin: 0; padding: 0; }
  html, body { width: 1200px; height: 1000px; overflow: hidden; }
  body {
    background: var(--backdrop);
    font-family: "Montserrat", Arial, sans-serif;
    position: relative;
  }
  .label {
    position: absolute;
    background: var(--label-white);
    display: flex;
    flex-direction: column;
    box-shadow: 0 4px 18px rgba(0,0,0,.12);
  }
  .brand {
    display: flex;
    align-items: center;
    justify-content: center;
    gap: 8px;
    color: var(--brand-green);
    font-weight: 700;
    font-size: 15px;
  }
  .brand-dot { width: 14px; height: 14px; border-radius: 50%; background: var(--brand-green); }
  .title-band {
    font-family: "Marcellus SC", Georgia, serif;
    color: var(--ink-dark);
    padding: 0 24px;
    display: flex;
    flex-direction: column;
    justify-content: center;
    white-space: nowrap;
  }
  .title-main { font-size: 40px; line-height: 1.05; }
  .title-with { font-size: 18px; line-height: 1; }
  .title-herb { font-size: 34px; line-height: 1.1; }
  .spacer { background: var(--label-white); }
  .info-band {
    flex: 1;
    color: #fff;
    text-align: center;
    display: flex;
    flex-direction: column;
    align-items: center;
    justify-content: flex-start;
    padding-top: 18px;
    gap: 8px;
    white-space: nowrap;
  }
  .claim { font-size: 10px; font-weight: 600; }
  .origin { font-size: 19px; font-weight: 700; }
  .weight { font-size: 11px; font-weight: 600; margin-top: 10px; }

  /* Organic */
  .label--organic { left: 60px; top: 300px; width: 300px; height: 420px; }
  .label--organic .brand { height: 90px; }
  .label--organic .title-band { background: var(--sage-soft); height: 110px; align-items: center; }
  .label--organic .title-main { font-size: 32px; }
  .label--organic .spacer { height: 60px; }
  .label--organic .claim { font-size: 8px; }
  .label--organic .origin { font-size: 15px; }
  .label--organic .weight { font-size: 9px; }

  .label--organic .info-band { background: var(--sage-band); }

  /* Cinnamon */
  .label--cinnamon { left: 390px; top: 160px; width: 360px; height: 480px; }
  .label--cinnamon .brand { height: 120px; }
  .label--cinnamon .title-band { background: var(--blush-soft); height: 150px; }
  .label--cinnamon .title-herb { color: var(--cinnamon); font-size: 28px; }
  .label--cinnamon .spacer { height: 70px; }
  .label--cinnamon .info-band { background: var(--blush-band); }

  /* Turmeric large */
  .label--turmeric { left: 780px; top: 120px; width: 360px; height: 480px; }
  .label--turmeric .brand { height: 120px; }
  .label--turmeric .title-band { background: var(--peach-soft); height: 150px; }
  .label--turmeric .title-herb { color: var(--turmeric); }
  .label--turmeric .spacer { height: 70px; }
  .label--turmeric .info-band { background: var(--peach-band); }

  /* Turmeric small */
  .label--mini { left: 830px; top: 650px; width: 240px; height: 250px; }
  .label--mini .brand { height: 50px; font-size: 10px; gap: 5px; }
  .label--mini .brand-dot { width: 9px; height: 9px; }
  .label--mini .title-band { background: var(--peach-soft); height: 70px; padding: 0 18px; }
  .label--mini .title-main { font-size: 22px; }
  .label--mini .title-with { font-size: 10px; }
  .label--mini .title-herb { font-size: 19px; color: var(--turmeric); }
  .label--mini .spacer { height: 36px; }
  .label--mini .info-band { background: var(--peach-band); padding-top: 10px; gap: 4px; }
  .label--mini .claim { font-size: 6px; }
  .label--mini .origin { font-size: 11px; }
  .label--mini .weight { font-size: 7px; margin-top: 4px; }
</style>
</head>
<body>

<section class="label label--organic">
  <div class="brand"><span class="brand-dot"></span>Amber Crest</div>
  <div class="title-band"><span class="title-main">Organic Honey</span></div>
  <div class="spacer"></div>
  <div class="info-band">
    <p class="claim">%100 Pure Naturally Grown Raw Honey with Ancient Herb</p>
    <p class="origin">MADE BY North Carolina BEES</p>
    <p class="weight">Net Wt. 16 oz.</p>
  </div>
</section>

<section class="label label--cinnamon">
  <div class="brand"><span class="brand-dot"></span>Amber Crest</div>
  <div class="title-band">
    <span class="title-main">Honey</span>
    <span class="title-with">with</span>
    <span class="title-herb">Cinnamon &amp; Clove</span>
  </div>
  <div class="spacer"></div>
  <div class="info-band">
    <p class="claim">%100 Pure Naturally Grown Raw Honey with Ancient Herb</p>
    <p class="origin">MADE BY North Carolina BEES</p>
    <p class="weight">Net Wt. 16 oz.</p>
  </div>
</section>

<section class="label label--turmeric">
  <div class="brand"><span class="brand-dot"></span>Amber Crest</div>
  <div class="title-band">
    <span class="title-main">Honey</span>
    <span class="title-with">with</span>
    <span class="title-herb">Raw Turmeric</span>
  </div>
  <div class="spacer"></div>
  <div class="info-band">
    <p class="claim">%100 Pure Naturally Grown Raw Honey with Ancient Herb</p>
    <p class="origin">MADE BY VIRGINIA BEES</p>
    <p class="weight">Net Wt. 16 oz.</p>
  </div>
</section>

<section class="label label--mini">
  <div class="brand"><span class="brand-dot"></span>Amber Crest</div>
  <div class="title-band">
    <span class="title-main">Honey</span>
    <span class="title-with">with</span>
    <span class="title-herb">Raw Turmeric</span>
  </div>
  <div class="spacer"></div>
  <div class="info-band">
    <p class="claim">%100 Pure Naturally Grown Raw Honey with Ancient Herb</p>
    <p class="origin">MADE BY VIRGINIA BEES</p>
    <p class="weight">Net Wt. 4 oz.</p>
  </div>
</section>

</body>
</html>
```